Business Card Design Project

Need a business card designed for a horse racing/gambling centered company.
Company name is BrightQuill.com.au
Company colours are similar to those in the logo.
Something clean and modern , designer given liberty to be creative.
Incorporate the logo is preferred.
Single or Double Sided fine
Must include :
Name
Mobile Number
Email Address
Reason: Apologies, I have been traveling unexpectedly with business and just need the extra two days to reply and give feedback before making a decision.
Industry/Entity Type
Business

```html
<!DOCTYPE html>
<html lang="en">
<head>
<meta charset="utf-8">
<title>BrightQuill.com.au – Business Card</title>
<link rel="stylesheet" href="https://fonts.googleapis.com/css2?family=Roboto+Condensed:wght@400;700&display=swap">
<style>
  :root {
    --stage: #8a8a8a;
    --ink: #050606;
    --teal: #25b3a3;
    --teal-deep: #138a7e;
    --white: #ffffff;
    --badge-ring: #f4f7f6;
    --font: "Roboto Condensed", "Arial Narrow", sans-serif;
  }
  * { box-sizing: border-box; margin: 0; padding: 0; }
  html, body {
    width: 1200px;
    height: 750px;
    overflow: hidden;
    background: var(--stage);
    font-family: var(--font);
  }
  .sheet {
    position: relative;
    width: 1200px;
    height: 750px;
    display: flex;
    align-items: center;
    justify-content: center;
    gap: 50px;
  }
  .card {
    position: relative;
    width: 540px;
    height: 309px;
    overflow: hidden;
    border-radius: 3px;
    box-shadow: 0 6px 18px rgba(0,0,0,0.35);
  }
  .card--back {
    background: linear-gradient(100deg, var(--ink) 0%, var(--ink) 38%, var(--teal-deep) 62%, var(--teal) 80%, var(--teal) 100%);
  }
  .card--front {
    background: linear-gradient(100deg, var(--ink) 0%, #0b1514 30%, var(--teal-deep) 58%, var(--teal) 78%, var(--teal) 100%);
  }
  .site-name {
    position: absolute;
    left: 48px;
    top: 142px;
    color: var(--white);
    font-weight: 700;
    font-size: 26px;
    letter-spacing: 0.2px;
  }
  .brand-badge {
    position: absolute;
    right: 34px;
    top: 52px;
    width: 205px;
    height: 205px;
    border-radius: 50%;
    background: var(--badge-ring);
    display: flex;
    align-items: center;
    justify-content: center;
  }
  .brand-badge__name {
    color: var(--ink);
    font-weight: 700;
    font-size: 26px;
  }
  .brand-watermark {
    position: absolute;
    left: 215px;
    top: 30px;
    width: 250px;
    height: 250px;
    border-radius: 50%;
    background: rgba(255,255,255,0.06);
  }
  .holder-name {
    position: absolute;
    left: 62px;
    top: 92px;
    color: var(--white);
    font-weight: 700;
    font-size: 25px;
  }
  .divider {
    position: absolute;
    left: 300px;
    top: 62px;
    width: 1px;
    height: 178px;
    background: rgba(255,255,255,0.85);
  }
  .contact {
    position: absolute;
    left: 322px;
    top: 160px;
    list-style: none;
    color: var(--white);
    font-size: 14px;
    line-height: 20px;
  }
  .contact__item {
    display: flex;
    align-items: center;
    gap: 6px;
  }
  .contact__icon { width: 12px; height: 12px; flex: none; }
</style>
</head>
<body>
  <main class="sheet">
    <section class="card card--back" aria-label="Card back">
      <p class="site-name">BrightQuill.com.au</p>
      <div class="brand-badge"><span class="brand-badge__name">BrightQuill</span></div>
    </section>

    <section class="card card--front" aria-label="Card front">
      <div class="brand-watermark" aria-hidden="true"></div>
      <h1 class="holder-name">Daniel Hart</h1>
      <div class="divider" aria-hidden="true"></div>
      <ul class="contact">
        <li class="contact__item">
          <svg class="contact__icon" viewBox="0 0 24 24" aria-hidden="true"><path fill="#fff" d="M6.6 10.8a15.1 15.1 0 0 0 6.6 6.6l2.2-2.2c.3-.3.7-.4 1-.2 1.1.4 2.3.6 3.6.6.6 0 1 .4 1 1V20c0 .6-.4 1-1 1A17 17 0 0 1 3 4c0-.6.4-1 1-1h3.5c.6 0 1 .4 1 1 0 1.3.2 2.5.6 3.6.1.3 0 .7-.2 1z"/></svg>
          <span>0455318762</span>
        </li>
        <li class="contact__item">
          <svg class="contact__icon" viewBox="0 0 24 24" aria-hidden="true"><rect x="2" y="5" width="20" height="14" rx="1.5" fill="#fff"/><path d="M3 6l9 7 9-7" fill="none" stroke="#138a7e" stroke-width="1.8"/></svg>
          <span>daniel@brightquill.com.au</span>
        </li>
      </ul>
    </section>
  </main>
</body>
</html>
```